Wedding Dried Apple Label / Name Place Card

We are looking for a simple but stylish label to be attached via string to a bag of dried apples from my family's fruit farm. The size of the label we think should be similar to the size of a business card. The packaging will be a plastic bag: 4" x 2" x 6".
We would like it to say something like:
Remy & Joss
Est. Sept 10, 2017
Dried Apple Slices
Product of Quenton Fruit Farm
________________
(We need a spot to write in the name of the person and a table number)
Our colors are also grey and navy, and would like these colors to be used.
We have uploaded a photo of the plastic bag.
Wedding

```html
<!DOCTYPE html>
<html lang="en">
<head>
<meta charset="utf-8">
<title>Remy &amp; Joss – Dried Apple Place Card</title>
<link rel="stylesheet" href="https://fonts.googleapis.com/css2?family=Playball&family=Source+Sans+3:wght@400;600&display=swap">
<style>
  :root {
    --backdrop: #cacaca;
    --card: #ffffff;
    --navy: #0b1186;
    --ink-dark: #3a3a3a;
    --ink-grey: #5a5a5a;
    --ink-soft: #666666;
  }
  html, body {
    margin: 0;
    padding: 0;
    width: 1200px;
    height: 766px;
    overflow: hidden;
    background: var(--backdrop);
  }
  .canvas {
    position: relative;
    width: 1200px;
    height: 766px;
  }
  .place-card {
    position: absolute;
    left: 121px;
    top: 109px;
    width: 958px;
    height: 548px;
    background: var(--card);
  }
  .frames {
    position: absolute;
    inset: 0;
  }
  .couple-names {
    position: absolute;
    left: 0;
    right: 0;
    top: 50px;
    margin: 0;
    text-align: center;
    font-family: "Playball", cursive;
    font-weight: 400;
    font-size: 92px;
    line-height: 1;
    color: var(--ink-dark);
  }
  .est-line {
    position: absolute;
    left: 0;
    right: 0;
    top: 180px;
    text-align: center;
    font-family: "Source Sans 3", sans-serif;
    font-size: 17px;
    color: var(--ink-soft);
  }
  .flourish {
    position: absolute;
    top: 163px;
    width: 92px;
    height: 52px;
    border-radius: 40% 40% 50% 50%;
    background: radial-gradient(ellipse at center, rgba(11,17,134,0.55), rgba(11,17,134,0.12) 70%, rgba(11,17,134,0));
  }
  .flourish.left { left: 300px; }
  .flourish.right { left: 565px; }
  .product {
    position: absolute;
    left: 0;
    right: 0;
    top: 238px;
    margin: 0;
    text-align: center;
    font-family: "Source Sans 3", sans-serif;
    font-size: 21px;
    line-height: 31px;
    color: var(--ink-soft);
  }
  .floral-corner {
    position: absolute;
    left: 54px;
    top: 300px;
    width: 292px;
    height: 208px;
    border-top-right-radius: 60% 70%;
    background: radial-gradient(ellipse at 20% 90%, rgba(11,17,134,0.75), rgba(11,17,134,0.25) 55%, rgba(11,17,134,0) 80%);
  }
  .guest-name {
    position: absolute;
    right: 163px;
    top: 368px;
    margin: 0;
    font-family: "Playball", cursive;
    font-size: 64px;
    line-height: 1;
    color: var(--ink-grey);
  }
  .table-number {
    position: absolute;
    right: 172px;
    top: 452px;
    font-family: "Source Sans 3", sans-serif;
    font-weight: 600;
    font-size: 26px;
    line-height: 1;
    color: var(--ink-grey);
  }
</style>
</head>
<body>
<div class="canvas">
  <section class="place-card">
    <svg class="frames" width="958" height="548" viewBox="0 0 958 548" aria-hidden="true">
      <rect x="39.5" y="18.5" width="895" height="496" fill="none" stroke="var(--navy)" stroke-width="3"/>
      <rect x="24.5" y="34.5" width="895" height="495" fill="none" stroke="var(--navy)" stroke-width="3"/>
    </svg>

    <h1 class="couple-names">Remy &amp; Joss</h1>
    <div class="flourish left" role="img" aria-label="Navy leaf flourish ornament"></div>
    <div class="est-line">Est. Sept 10, 2017</div>
    <div class="flourish right" role="img" aria-label="Navy leaf flourish ornament"></div>

    <p class="product">Dried Apple Slices<br>Product of Quenton Fruit Farm</p>

    <div class="floral-corner" role="img" aria-label="Navy floral vine illustration with dots and blossoms"></div>

    <p class="guest-name">Mara Linden</p>
    <div class="table-number">Table 1</div>
  </section>
</div>
</body>
</html>
```